Business Card Design for a Handbags business

We are modernising our handbags website (see attached file for new front page) and are in need of a modern business card and a related design we can use on a small marquee at the markets, on letterhead, emails etc.

As the leather handbags we mostly import are from Italy, we want a smart modern European feel to the design. We are currently thinking about changing the name of the business from Meadowlark Handbags (see www.meadowlarkhandbags.com.au) to Vantera Handbags. Also open to other suggestions you may have that communicates the European influence and quality.

Target Market(s)

25-65 year old women (and some men)

Industry/Entity Type

Business

Contact Information for Business Card

Single or double sided - whichever creates more of an impact

Font styles to use
Serif
Sans Serif

Requirements
Must have
• Clean crisp look, slightly Italian or European look and feel to reflect where the handbags are imported from
Nice to have
• open to ideas

```html
<!DOCTYPE html>
<html lang="en">
<head>
<meta charset="utf-8">
<title>Vantera Handbags And Accessories – Business Card</title>
<link href="https://fonts.googleapis.com/css2?family=Lora:wght@400;700&display=swap" rel="stylesheet">
<style>
  :root {
    --backdrop: #8f8e8f;
    --card-white: #ffffff;
    --ink: #0a0a0a;
    --frame-black: #050505;
    --rule: #2a2a2a;
    --photo-warm: #c9a27e;
    --photo-light: #e9e4dc;
    --photo-gold: #d9bf7a;
    --photo-red: #c8302c;
    --photo-grey: #b9b7b4;
  }
  * { box-sizing: border-box; margin: 0; padding: 0; }
  html, body { width: 1189px; height: 1200px; overflow: hidden; }
  body { background: var(--backdrop); font-family: 'Lora', Georgia, serif; color: var(--ink); position: relative; }

  .card { position: absolute; left: 171px; width: 856px; height: 489px; box-shadow: 2px 3px 4px rgba(0,0,0,0.35); }
  .card--front { top: 66px; background: var(--card-white); }
  .card--back { top: 627px; background: var(--frame-black); }

  .front-frame { position: absolute; left: 43px; top: 38px; width: 772px; height: 413px; background: var(--frame-black); }
  .front-panel { position: absolute; left: 17px; top: 17px; width: 738px; height: 379px; background: var(--card-white); }

  .photo { position: absolute; border: 1px solid #cfcfcf; }
  .photo--model-beret   { left: 5px;   top: 1px;   width: 173px; height: 165px; background: linear-gradient(135deg, #b48a62, var(--photo-warm) 60%, #e6d6c4); }
  .photo--tan-tote      { left: 5px;   top: 173px; width: 173px; height: 116px; background: linear-gradient(180deg, #ece9e4, #b8a08a); }
  .photo--white-dress   { left: 184px; top: 1px;   width: 110px; height: 288px; background: linear-gradient(180deg, #d8d6d2, var(--photo-light) 55%, #bdb8b0); }
  .photo--gold-bag      { left: 300px; top: 1px;   width: 225px; height: 184px; background: linear-gradient(120deg, #cdb89a, var(--photo-gold) 60%, #b99a4e); }
  .photo--red-bag-floor { left: 300px; top: 191px; width: 225px; height: 98px;  background: linear-gradient(90deg, #f1ebe4, var(--photo-red) 45%, #efe7dc); }
  .photo--grey-case     { left: 531px; top: 1px;   width: 202px; height: 98px;  background: linear-gradient(90deg, #9ea3aa, var(--photo-grey) 50%, #8b7f78); }
  .photo--red-bag-wall  { left: 531px; top: 106px; width: 202px; height: 183px; background: linear-gradient(180deg, #eeeae6, #e6ddd6 45%, var(--photo-red)); }

  .brand-title { position: absolute; left: 0; right: 0; font-weight: 700; font-size: 36px; line-height: 1.2; text-align: center; letter-spacing: 0.2px; white-space: nowrap; }
  .front-panel .brand-title { top: 308px; }

  .back-panel { position: absolute; left: 43px; top: 36px; width: 772px; height: 413px; background: var(--card-white); }
  .back-rule { position: absolute; left: 15px; top: 13px; width: 740px; height: 383px; border: 1.5px solid var(--rule); }
  .back-faded-bags { position: absolute; left: 150px; top: 130px; width: 472px; height: 248px; opacity: 0.14;
    background: linear-gradient(90deg, #4a4a4a, #b4533f 45%, #6b3a2e 65%, #c9c2b8); border-radius: 24px 24px 4px 4px; }
  .back-panel .brand-title { top: 78px; }

  .contact { position: absolute; left: 0; right: 0; text-align: center; line-height: 1.2; white-space: nowrap; }
  .contact__name { top: 170px; font-weight: 700; font-size: 30px; }
  .contact__phone { top: 210px; font-size: 23px; }
  .contact__city { top: 265px; font-size: 23px; }
  .contact__web { top: 294px; font-size: 23px; letter-spacing: 0.3px; }
</style>
</head>
<body>
  <section class="card card--front">
    <div class="front-frame">
      <div class="front-panel">
        <div class="photo photo--model-beret" role="img" aria-label="Model in a leopard beret holding a quilted cream handbag"></div>
        <div class="photo photo--tan-tote" role="img" aria-label="Tan leather tote with dark handles"></div>
        <div class="photo photo--white-dress" role="img" aria-label="Model in a white dress carrying a cream handbag"></div>
        <div class="photo photo--gold-bag" role="img" aria-label="Model holding a gold woven handbag"></div>
        <div class="photo photo--red-bag-floor" role="img" aria-label="Model lying beside a red leather handbag"></div>
        <div class="photo photo--grey-case" role="img" aria-label="Model holding a grey structured case bag"></div>
        <div class="photo photo--red-bag-wall" role="img" aria-label="Model with a red leather handbag against a pale wall"></div>
        <h1 class="brand-title">Vantera Handbags And Accessories</h1>
      </div>
    </div>
  </section>

  <section class="card card--back">
    <div class="back-panel">
      <div class="back-rule"></div>
      <div class="back-faded-bags" role="img" aria-label="Faded group of assorted handbags"></div>
      <h2 class="brand-title">Vantera Handbags And Accessories</h2>
      <p class="contact contact__name">Clara Whitfield</p>
      <p class="contact contact__phone">P: 0412 630 918</p>
      <p class="contact contact__city">Brisbane</p>
      <p class="contact contact__web">www.meadowlarkhandbags.com.au</p>
    </div>
  </section>
</body>
</html>
```